Regenerative Medicine Brochure

I want a clean modern bi-fold or tri-fold brochure. We offer non-surgical joint repair for knees, shoulders, and hips. We have many services available including regenerative medicine including stem cell allograft, palatelet rich plasma, prolotherapy, triggerpoint injection, chiropractic and rehab therapies. We are a modern multidisciplinary clinic in coastal California. My logo is already complete and is a vibrant green color. I prefer lots of white space with some areas for service description and what conditions may benefit from the services. Design should convey modern treatments, upscale office and practice, and our target audience is older adults who want to maintain an active pain-free lifestyle.

Target Market(s)

Sports injuries, athletes, seniors who are active, knee pain, shoulder pain, arthritis.

Industry/Entity Type

Alternative Medicine

Font styles to use
Serif

Colors
9bcb3c

Requirements
Must have
• Small white space where we can write date, time, location of next event/class. Colors in brochure to coordinate with logo colors provided.

```html
<!DOCTYPE html>
<html lang="en">
<head>
<meta charset="utf-8">
<title>Regenerative Medicine Brochure – Inside Spread</title>
<link rel="stylesheet" href="https://fonts.googleapis.com/css2?family=Crimson+Text:ital,wght@0,400;0,700;1,400;1,700&display=swap">
<style>
  :root {
    --green: #52b848;
    --blue: #6282b3;
    --heading-blue: #4c6c96;
    --ink: #231f20;
    --paper: #ffffff;
  }
  * { margin: 0; padding: 0; box-sizing: border-box; }
  html, body { width: 1200px; height: 934px; overflow: hidden; background: var(--paper); }
  .spread {
    position: relative;
    width: 1200px;
    height: 934px;
    font-family: "Crimson Text", Georgia, serif;
    color: var(--ink);
    font-size: 19.6px;
    line-height: 22.1px;
  }
  .backdrop { position: absolute; inset: 0; width: 1200px; height: 934px; }
  .block { position: absolute; width: 350px; }
  .col-1 { left: 36px; }
  .col-2 { left: 430px; }
  .col-3 { left: 821px; }
  .panel-heading {
    font-weight: 700;
    font-style: italic;
    font-size: 22.5px;
    line-height: 22.4px;
    color: var(--heading-blue);
  }
  .panel-3 .panel-heading { color: var(--paper); }
  .area-list {
    list-style: none;
    margin-top: 21px;
    margin-left: 54px;
  }
  .area-list li {
    color: var(--green);
    font-style: italic;
    font-size: 19.8px;
    letter-spacing: 0.5px;
    line-height: 22.1px;
  }
  .area-list li::before {
    content: "✳";
    display: inline-block;
    width: 23px;
    font-style: normal;
    font-size: 12px;
    vertical-align: 2px;
  }
</style>
</head>
<body>
<main class="spread">
  <svg class="backdrop" viewBox="0 0 2184 1700" preserveAspectRatio="none" aria-hidden="true">
    <polygon fill="var(--green)" points="0,0 690,0 0,462"/>
    <polygon fill="var(--green)" points="712,0 745,0 0,500 0,478"/>
    <polygon fill="var(--green)" points="455,1700 745,1505 745,1530 492,1700"/>
    <polygon fill="var(--green)" points="518,1700 745,1548 745,1700"/>
    <polygon fill="var(--blue)" points="0,643 1455,643 1455,0 2184,0 2184,505 1455,990 0,990"/>
    <polygon fill="var(--blue)" points="0,1000 1455,1000 2184,515 2184,545 1455,1028 0,1028"/>
  </svg>

  <p class="block col-1" style="top:145px">Regenerative medicine may be used in the following areas:</p>
  <ul class="block col-1 area-list" style="top:180px">
    <li>Shoulder</li>
    <li>Elbow</li>
    <li>Wrist</li>
    <li>Hip</li>
    <li>Knee</li>
    <li>Ankle</li>
  </ul>
  <p class="block col-1" style="top:367px">There are many additional types of bone and soft tissue problems, including arthritis, that these injections may benefit.</p>
  <p class="block col-1" style="top:567px">With regenerative medicine and amniotic allograft treatments, the team supports the natural healing abilities of your body without the need for drugs or surgical repair and painful recovery. However, not all forms of regenerative medicine are equal. At Harborline Spine &amp; Joint, the team only works with the best regenerative medicine labs to ensure that the right kind of products are selected and that they are of the best quality and highest safety.</p>

  <h2 class="block col-2 panel-heading" style="top:80px">How does regenerative medicine work?</h2>
  <p class="block col-2" style="top:145px">The team uses lab-grade products that are sterilized and processed to inject into the injured area. Once injected, it is thought that these powerful products differentiate into a variety of tissues to trigger your own body to repair damaged tissues. This damage may involve minor tears in muscles, ligaments, and tendons, or cartilage and meniscus breakdown in joints.</p>
  <p class="block col-2" style="top:367px">Regenerative medicine products contain the basic building blocks of the body tissues — including proteins, amino acids, and cytokines — responsible for healing and tissue growth. They also provide anti-inflammatory benefits by promoting repair of tissues affected by inflammation.</p>
  <p class="block col-2" style="top:567px">While some inflammation is normal and has a benefit to healing injuries, long-term inflammation causes pain, swelling, and further damage to tissues. When you experience too much inflammation, it does more harm than good. Instead of constantly relying on anti-inflammatory medications, regenerative products may be able to correct the problem at the source and reduce the production of natural inflammatory chemicals so you can heal.</p>

  <section class="panel-3">
    <h2 class="block col-3 panel-heading" style="top:80px">What can I expect from regenerative medicine treatments?</h2>
    <p class="block col-3" style="top:145px">During your visit, the team begins with a consultation and physical exam to determine if you’re a candidate for regenerative medicine. They ask about your symptoms, condition, overall health, and lifestyle. If you’re a candidate, the team then explains the procedure and what to expect both during and afterward.</p>
    <p class="block col-3" style="top:367px">For the procedure, the team first cleans your skin and applies a topical numbing cream to your skin, if needed. Next, the team injects regenerative products into the treatment area. You may feel a slight pinch or burning sensation during the injection. The injection takes less than five minutes and you can return to your usual activities the same day. Mild soreness at the injection site is possible for two to three days.</p>
    <p class="block col-3" style="top:611px">Over the coming weeks and months, the injected products help repair damaged tissues at the treatment site. Most people notice results after two months. Follow-up care may be recommended based on your condition and initial results. The team has seen dramatic results with regenerative medicine treatments, however, individual results can vary. Speak to the team to see if regenerative medicine is right for you.</p>
  </section>
</main>
</body>
</html>
```